Start-up braucht modernes/hochwertiges Getränkeetikett
Zielgruppe
Wir sind ein modernes, nachhaltiges Start-up, welches eine neue Getränkekategorie auf den Markt bringt. Ein sogenanntes Elektrolyt-Getränk mit dem Namen KLORV5. Es ist abgefüllt in eine 500 ml Flasche und enthält Magnesium, Kalzium, Kalium, und Natrium. Diese Stoffe (Elektrolyte) dienen der körperlichen Hydrierung. Zu Dehydrierung kann es durch Hitze, Alkohol, Sport oder Krankheit kommen. Krankheit liegt bei uns allerdings nicht im Fokus. In unserer Zielgruppe befinden sich hauptsächlich Personen im Alter von 18 - 29 Jahren.
Die Geschmacksrichtung ist Zitrone-Limette.
Aufgabenstellung
Das Etikett soll:
- MODERN, SCHLICHT und HOCHWERTIG sein, so dass es im Supermarkt hervorsticht
- erkenntlich machen, dass die Stoffe Magnesium, Natrium, Kalzium und Kalium enthalten sind
- sich farblich deutlich von der Farbe des Inhalts (weiß) abheben. (Vorzugsweise mit einem hellen Blau, türkis)
- für unsere junge Zielgruppe ansprechend sein
- ebenfalls auf die Geschmacksrichtung (Zitrone-Limette) hinweisen, und zwar so, dass wenn man eine weitere Geschmacksrichtung auf den Markt bringen möchte, diese leicht angepasst werden kann.
- nicht nach einem Energydrink oder einem typischen Sportgetränk aussehen
- unter dem Namen den Slogan 'Elektrolyt-Getränk' stehen haben
-Das Etikett ist nicht dursichtig sondern besteht aus Papier
Der Name sowie das Logo können selbstverständlich farblich verändert werden. Bei dem Logo können auch größere Änderungen vollzogen werden.
Bitte beachten Sie die unten zu stehenden Regler um sich einen guten Überblick über unsere Vorstellungen zu verschaffen. Die Platzierung des EAN-Code ist für ihr Design irrelevat .
Bei Unklarheiten gerne nachfragen!

```html
<!DOCTYPE html>
<html lang="de">
<head>
<meta charset="utf-8">
<title>KLORV5 Etikett</title>
<link rel="stylesheet" href="https://fonts.googleapis.com/css2?family=Lexend:wght@300;400;700&display=swap">
<style>
  :root {
    --stage: #d7d8da;
    --paper-light: #f6f6f7;
    --paper-dark: #e9eaeb;
    --band-top: #5f6b72;
    --band-bottom: #3f4d55;
    --band-ink: #eef0f1;
    --ingredient-ink: #b4b8bc;
    --flavour-ink: #6c7175;
  }
  html, body {
    margin: 0;
    padding: 0;
    width: 667px;
    height: 1200px;
    overflow: hidden;
    background: var(--stage);
  }
  .label {
    position: absolute;
    left: 23px;
    top: 118px;
    width: 620px;
    height: 963px;
    display: block;
  }
  .label-paper { fill: url(#paperShade); }
  .brand-band { fill: url(#bandShade); }
  .brand-mark { fill: none; stroke: var(--band-ink); stroke-width: 2.5; }
  .brand-name {
    font-family: "Lexend", sans-serif;
    font-weight: 700;
    font-size: 150px;
    fill: var(--band-ink);
  }
  .brand-tagline {
    font-family: "Lexend", sans-serif;
    font-weight: 400;
    font-size: 19px;
    fill: var(--band-ink);
  }
  .ingredient {
    font-family: "Lexend", sans-serif;
    font-weight: 300;
    font-size: 16px;
    letter-spacing: 1px;
    fill: var(--ingredient-ink);
  }
  .flavour {
    font-family: "Lexend", sans-serif;
    font-weight: 300;
    font-size: 17px;
    letter-spacing: 1px;
    fill: var(--flavour-ink);
  }
</style>
</head>
<body>
<svg class="label" viewBox="0 0 620 963" xmlns="http://www.w3.org/2000/svg">
  <defs>
    <linearGradient id="paperShade" x1="0" y1="0" x2="1" y2="0">
      <stop offset="0" stop-color="var(--paper-dark)"/>
      <stop offset="0.5" stop-color="var(--paper-light)"/>
      <stop offset="1" stop-color="var(--paper-dark)"/>
    </linearGradient>
    <linearGradient id="bandShade" x1="0" y1="0" x2="0" y2="1">
      <stop offset="0" stop-color="var(--band-top)"/>
      <stop offset="1" stop-color="var(--band-bottom)"/>
    </linearGradient>
  </defs>

  <rect class="label-paper" x="0" y="0" width="620" height="963"/>
  <rect class="brand-band" x="204" y="0" width="191" height="963"/>

  <circle class="brand-mark" cx="300" cy="194" r="62"/>

  <text class="brand-name" transform="translate(352 875) rotate(-90)" textLength="600" lengthAdjust="spacingAndGlyphs">KLORV5</text>
  <text class="brand-tagline" transform="translate(380 630) rotate(-90)" textLength="250" lengthAdjust="spacingAndGlyphs">Elektrolyt-Getränk</text>

  <g class="ingredients">
    <text class="ingredient" transform="translate(63 870) rotate(-90)">Magnesium</text>
    <text class="ingredient" transform="translate(94 870) rotate(-90)">Natrium</text>
    <text class="ingredient" transform="translate(129 870) rotate(-90)">Kalcium</text>
    <text class="ingredient" transform="translate(171 870) rotate(-90)">Kalium</text>
  </g>

  <g class="flavours">
    <text class="flavour" transform="translate(447 870) rotate(-90)">Zitrone</text>
    <text class="flavour" transform="translate(492 870) rotate(-90)">Limette</text>
  </g>
</svg>
</body>
</html>
```